General Dental Office Business Card

I run a private general dental office in southern California, and would like a refresh/redesign of my business card. I focus on quality care rather than volume. The email address on the uploaded current card should be updated to: info@marbleshoredental.example. The current card's logo is a deboss, but I am open to other ideas. The logo can be refreshed, but it is something that's been with me since the beginning of the office, so I wouldn't want a drastic redesign.
Target Market(s)
Adults 18-99, whoever needs dental services
Industry/Entity Type
Healthcare/Dental
Contact Information for Business Card
Name, Address, Phone, email
Colors
Designer to choose colors to be used in the design.
Requirements
Must have
- Logo (Same as original one in the uploaded file), space on back for appointment time/date

```html
<!DOCTYPE html>
<html lang="en">
<head>
<meta charset="utf-8">
<title>Marble Shore Dental – Business Card</title>
<link href="https://fonts.googleapis.com/css2?family=Lato:wght@400;700&display=swap" rel="stylesheet">
<style>
  :root {
    --stage-deep: #0077c0;
    --stage-bright: #00aeea;
    --stage-pale: #cdeaf7;
    --card-front: #86cfea;
    --card-front-light: #a6dcf0;
    --strip: #d5eff9;
    --field: #dff3fb;
    --accent: #7fd0ee;
    --accent-text: #6cc6e8;
    --back-light: #8c8c90;
    --back-dark: #29292b;
    --white: #ffffff;
  }
  * { box-sizing: border-box; margin: 0; padding: 0; }
  html, body { width: 1200px; height: 1200px; overflow: hidden; }
  body { font-family: "Lato", sans-serif; }

  .canvas {
    position: relative; width: 1200px; height: 1200px;
    background: linear-gradient(90deg, var(--stage-deep) 0%, var(--stage-bright) 50%, var(--stage-pale) 50%, var(--stage-pale) 100%);
  }

  .card {
    position: absolute; left: 269px; width: 662px; height: 378px;
    overflow: hidden; box-shadow: 0 4px 14px rgba(0,0,0,.3);
  }
  .card--front { top: 198px; }
  .card--back { top: 630px; background: linear-gradient(105deg, var(--back-light) 0%, #5c5c5f 45%, var(--back-dark) 100%); }

  .front-pattern {
    position: absolute; inset: 0;
    background:
      radial-gradient(circle at 50% 45%, rgba(255,255,255,.22) 0%, rgba(255,255,255,0) 60%),
      linear-gradient(135deg, var(--card-front-light) 0%, var(--card-front) 100%);
  }
  .front-mark {
    position: absolute; left: 185px; top: 16px; width: 290px; height: 290px;
    border-radius: 50%; border: 18px solid rgba(255,255,255,.38);
    display: flex; align-items: center; justify-content: center; text-align: center;
    font-size: 40px; font-weight: 700; line-height: 1.15; color: rgba(255,255,255,.45);
  }

  .field {
    position: absolute; left: 0; background: var(--field);
    border-radius: 0 26px 26px 0;
  }
  .field--date { top: 24px; width: 215px; height: 50px; }
  .field--time { top: 84px; width: 183px; height: 48px; }
  .field-line { position: absolute; left: 0; height: 2px; background: var(--accent); }
  .field--date .field-line { top: 25px; width: 206px; }
  .field--time .field-line { top: 25px; width: 174px; }
  .field-label {
    position: absolute; left: 22px; top: 29px; font-size: 13px; font-weight: 700; color: var(--accent-text);
  }

  .front-strip {
    position: absolute; left: 551px; top: 0; width: 111px; height: 378px; background: var(--strip);
  }
  .front-name {
    position: absolute; left: 590px; top: 30px; height: 318px; width: 44px;
    writing-mode: vertical-rl; transform: rotate(180deg);
    font-size: 33px; font-weight: 700; color: var(--accent); text-align: center; white-space: nowrap;
  }

  .back-name {
    position: absolute; left: 20px; top: 50px; height: 280px; width: 36px;
    writing-mode: vertical-rl; font-size: 27px; color: var(--accent); white-space: nowrap; text-align: center;
  }
  .brand-mark {
    position: absolute; left: 65px; top: 90px; width: 168px; height: 168px;
    border-radius: 50%; border: 5px solid var(--accent);
    display: flex; align-items: center; justify-content: center; text-align: center;
    font-size: 20px; line-height: 1.2; color: var(--accent);
  }

  .dentist { position: absolute; right: 66px; top: 68px; text-align: right; color: var(--accent); }
  .dentist-name { font-size: 26px; font-weight: 700; }
  .dentist-role { font-size: 19px; margin-top: 4px; }
  .dentist-rule { position: absolute; left: 304px; top: 130px; width: 334px; height: 2px; background: var(--accent); }

  .contact { position: absolute; right: 66px; text-align: right; font-size: 19px; color: var(--accent); line-height: 26px; }
  .contact--address { top: 164px; }
  .contact--phone { top: 232px; }
  .contact--email { top: 273px; }
  .contact--web { top: 315px; }

  .icon-tab {
    position: absolute; left: 602px; width: 60px; height: 32px;
    background: var(--accent); border-radius: 8px 0 0 8px;
  }
  .icon-tab svg { position: absolute; left: 3px; top: 2px; }
</style>
</head>
<body>
<div class="canvas">

  <section class="card card--front" aria-label="Card front with appointment fields">
    <div class="front-pattern" role="img" aria-label="Soft repeating brand pattern in pale blue"></div>
    <div class="front-mark">Marble<br>Shore<br>Dental</div>

    <div class="field field--date"><span class="field-line"></span><span class="field-label">Appointment Date</span></div>
    <div class="field field--time"><span class="field-line"></span><span class="field-label">Time</span></div>

    <div class="front-strip"></div>
    <div class="front-name">Marble Shore Dental</div>
  </section>

  <section class="card card--back" aria-label="Card back with contact details">
    <div class="back-name">Marble Shore Dental</div>
    <div class="brand-mark">Marble Shore<br>Dental</div>

    <div class="dentist">
      <div class="dentist-name">Daniel R. Okafor DDS</div>
      <div class="dentist-role">General Dentistry</div>
    </div>
    <div class="dentist-rule"></div>

    <div class="contact contact--address">2180 Harbor View Lane<br>Marble Shore, CA 92600</div>
    <div class="contact contact--phone">555-014-2828</div>
    <div class="contact contact--email">info@marbleshoredental.example</div>
    <div class="contact contact--web">www.marbleshoredental.example</div>

    <div class="icon-tab" style="top:190px">
      <svg width="28" height="28" viewBox="0 0 28 28" aria-hidden="true">
        <circle cx="14" cy="14" r="12.5" fill="none" stroke="var(--white)" stroke-width="2"/>
        <path d="M14 21 C10 16 9 14 9 11.5 a5 5 0 0 1 10 0 C19 14 18 16 14 21z" fill="none" stroke="var(--white)" stroke-width="1.6"/>
        <circle cx="14" cy="11.5" r="1.8" fill="var(--white)"/>
      </svg>
    </div>
    <div class="icon-tab" style="top:232px">
      <svg width="28" height="28" viewBox="0 0 28 28" aria-hidden="true">
        <circle cx="14" cy="14" r="12.5" fill="none" stroke="var(--white)" stroke-width="2"/>
        <path d="M9.5 7.5 l3 3 -1.8 2 c1 2 2.5 3.5 4.5 4.5 l2-1.8 3 3 -2 2 c-5 -0.5 -10 -5.5 -10.7 -10.7z" fill="none" stroke="var(--white)" stroke-width="1.6" stroke-linejoin="round"/>
      </svg>
    </div>
    <div class="icon-tab" style="top:275px">
      <svg width="28" height="28" viewBox="0 0 28 28" aria-hidden="true">
        <circle cx="14" cy="14" r="12.5" fill="none" stroke="var(--white)" stroke-width="2"/>
        <rect x="7" y="9" width="14" height="10" fill="none" stroke="var(--white)" stroke-width="1.6"/>
        <path d="M7 9 l7 6 7-6 M7 19 l5-5 M21 19 l-5-5" fill="none" stroke="var(--white)" stroke-width="1.4"/>
      </svg>
    </div>
    <div class="icon-tab" style="top:318px">
      <svg width="28" height="28" viewBox="0 0 28 28" aria-hidden="true">
        <circle cx="14" cy="14" r="12.5" fill="none" stroke="var(--white)" stroke-width="2"/>
        <circle cx="14" cy="14" r="7" fill="none" stroke="var(--white)" stroke-width="1.4"/>
        <path d="M7 14 h14 M14 7 v14 M8.5 10.5 h11 M8.5 17.5 h11" fill="none" stroke="var(--white)" stroke-width="1.1"/>
        <ellipse cx="14" cy="14" rx="3.2" ry="7" fill="none" stroke="var(--white)" stroke-width="1.1"/>
      </svg>
    </div>
  </section>

</div>
</body>
</html>
```